The most amazing design opportunity you will ever get - Plus we may even through in some shares!

We need a new look and feel for our website, something that will knock the socks off our competitors. Something fresh, functional, dynamic and awesome.

Take a look at the attached brief and see if this is something you can get you head around to come up with something just amazing.

Reason: need more designs

A key to your success is to base your design on the Visual Language (colours Black with Orange on white background, integration of cogs, font, style) and remember that our target audience is BUSINESS and the key thing that we are about is INSIGHTS, so if you can include some subtle design that requires insight to use - Perfect!

```html
<!DOCTYPE html>
<html lang="en">
<head>
<meta charset="utf-8">
<title>Gearwise Insight – Member Login</title>
<link href="https://fonts.googleapis.com/css2?family=Oswald:wght@300;400;500&family=Roboto:wght@400;500;700&family=Quicksand:wght@400;500&family=Montserrat:wght@700;800&display=swap" rel="stylesheet">
<style>
:root{
  --orange:#f7941d;
  --orange-dark:#e07b0c;
  --ink:#1e1e1e;
  --dark:#2b2b2b;
  --dark-2:#3a3a3a;
  --bar:#262626;
  --grey:#8c8c8c;
  --grey-light:#d9d9d9;
  --paper:#e9e9e9;
  --white:#ffffff;
  --blue:#1b6dc1;
  --blue-icon:#2b7fd6;
  --label:#f2f2f2;
}
*{box-sizing:border-box;margin:0;padding:0}
html,body{width:963px;height:1200px;overflow:hidden;background:var(--paper)}
.stage{position:relative;width:1201px;height:1496px;transform:scale(.8018);transform-origin:0 0;font-family:Roboto,Arial,sans-serif;background:var(--paper)}
.abs{position:absolute}

/* top stats bar */
.statbar{position:absolute;left:0;top:0;width:1201px;height:45px;background:linear-gradient(#3a3a3a,#1c1c1c)}
.view-switch{position:absolute;left:124px;top:0;width:167px;height:45px;background:var(--orange)}
.toggle{position:absolute;height:28px;border-radius:14px;background:linear-gradient(#f4f4f4,#cfcfcf);box-shadow:inset 0 1px 2px rgba(0,0,0,.3);font-family:Oswald,sans-serif;font-weight:300;font-size:14px;display:flex;align-items:center;padding:0 12px;gap:12px}
.toggle .off{color:#9a9a9a}
.toggle .on{color:var(--orange)}
.stat{position:absolute;top:0;height:45px;display:flex;align-items:center;gap:8px;border-left:1px solid #4a4a4a;padding-left:10px;width:115px}
.stat .ico{width:30px;height:30px;border-radius:50%;background:var(--orange);flex:none;display:flex;align-items:center;justify-content:center}
.stat .txt{font-family:Oswald,sans-serif;font-weight:300;line-height:16px;font-size:14px}
.stat .num{color:var(--orange)}
.stat .lbl{color:var(--white)}

/* header */
.header{position:absolute;left:168px;top:45px;width:862px;height:150px;background:linear-gradient(#f3f3f3,#d6d6d6)}
.brand{position:absolute;left:18px;top:62px;font-family:Montserrat,sans-serif;font-weight:800;font-size:38px;line-height:44px;color:var(--ink);letter-spacing:-1px}
.tagline{position:absolute;left:230px;top:47px;font-family:Roboto,sans-serif;font-size:21px;line-height:24.5px;color:#2a2a2a}
.news{position:absolute;left:530px;width:500px;height:32px;background:linear-gradient(#2e2e2e,#151515);border-radius:0 2px 2px 0;display:flex;align-items:center;gap:10px;padding-left:4px;font-family:Oswald,sans-serif;font-weight:300;font-size:14px;color:var(--white)}
.news .ico{width:26px;height:26px;border-radius:50%;background:var(--blue-icon);flex:none}

/* nav */
.nav{position:absolute;left:0;top:200px;width:1201px;height:45px;background:var(--blue)}
.nav .strip{position:absolute;left:0;top:32px;width:1201px;height:13px;background:#1a5faa}
.tab{position:absolute;top:3px;height:28px;padding:0 10px;display:flex;align-items:center;font-family:Oswald,sans-serif;font-weight:300;font-size:15px;color:var(--white);background:linear-gradient(#5a5a5a,#2d2d2d);border-radius:10px 10px 0 0}
.tab.home{background:var(--blue)}
.tab.active{background:linear-gradient(#fbab3c,var(--orange-dark))}

/* login area */
.page{position:absolute;left:121px;top:245px;width:960px;height:500px;background:var(--white)}
.card{position:absolute;left:248px;top:292px;width:704px;height:426px;border-radius:80px;background:radial-gradient(circle at 60% 45%,#4a4a4a,#1f1f1f 75%);border:5px solid #9a9a9a;box-shadow:0 0 0 2px #ddd}
.card h1{position:absolute;left:0;right:0;top:12px;text-align:center;font-family:Quicksand,sans-serif;font-weight:400;font-size:34px;color:var(--orange)}
.card .rule{position:absolute;left:210px;width:290px;top:55px;height:1px;background:linear-gradient(90deg,transparent,#999,transparent)}
.field-label{position:absolute;font-size:13.5px;color:var(--white);font-family:Roboto,sans-serif}
.field{position:absolute;height:30px;border-radius:12px;background:linear-gradient(#d8d8d8,#9c9c9c);box-shadow:0 1px 0 #666}
.pill{position:absolute;height:22px;border-radius:11px;background:linear-gradient(#5a5a5a,#3a3a3a);color:var(--white);font-size:13.5px;display:flex;align-items:center;padding:0 10px;font-family:Roboto,sans-serif}
.login-btn{position:absolute;left:190px;top:316px;width:80px;height:30px;border-radius:6px;background:linear-gradient(#ffd25a,var(--orange));color:#222;font-family:Quicksand,sans-serif;font-weight:500;font-size:18px;display:flex;align-items:center;justify-content:center}
.seal{position:absolute;border-radius:50%}
.back{position:absolute;left:570px;top:300px;color:var(--white);font-size:11.5px;line-height:14px}

/* footer */
.stripes{position:absolute;left:0;top:745px;width:1201px;height:18px;background:linear-gradient(var(--orange) 0 4px,#c96a0e 4px 7px,var(--orange) 7px 10px,#3a3a3a 10px)}
.footer{position:absolute;left:0;top:763px;width:1201px;height:733px;background:radial-gradient(ellipse at 50% 30%,#4a4a4a,#262626 70%)}
.hub{position:absolute;width:170px;height:170px;border-radius:50%;background:radial-gradient(circle,#fff 0 52%,#ccc 60%,#e0e0e0 64%,#9b9b9b 100%);box-shadow:0 3px 6px rgba(0,0,0,.6)}
.hub::before{content:"";position:absolute;inset:15px;border-radius:50%;border:2px solid var(--orange)}
.hub .mini{position:absolute;left:0;right:0;top:32px;text-align:center;font-family:Montserrat,sans-serif;font-weight:800;font-size:14px;color:#2a2a2a}
.hub .title{position:absolute;left:0;right:0;top:62px;text-align:center;font-family:Oswald,sans-serif;font-weight:300;font-size:21px;line-height:25px;color:#1f1f1f;letter-spacing:1px}
.lbl{position:absolute;font-size:13px;color:var(--white);line-height:15px;font-family:Roboto,sans-serif}
.lbl.hot{color:var(--orange)}
.cat{position:absolute;font-size:10px;font-weight:500;color:var(--white);line-height:12.5px;letter-spacing:.3px}
.cat.r{text-align:right}
.cat.hot{color:var(--orange)}
.social{position:absolute;left:1021px;width:28px;height:28px;background:#8a8a8a}
.round{position:absolute;left:1020px;width:30px;height:30px;border-radius:50%;background:#9a9a9a;display:flex;align-items:center;justify-content:center}
.baseline{position:absolute;left:215px;top:1455px;width:770px;height:1px;background:#6a6a6a}
.foot-brand{position:absolute;left:538px;top:1436px;width:66px;height:36px;border-radius:6px;background:var(--white);display:flex;align-items:center;justify-content:center;font-family:Montserrat,sans-serif;font-weight:800;font-size:11px;color:var(--ink)}
.copy{position:absolute;left:0;right:0;top:1478px;text-align:center;font-size:10px;letter-spacing:2px;color:var(--white);font-weight:500}
</style>
</head>
<body>
<div class="stage">

  <svg width="0" height="0" style="position:absolute">
    <defs>
      <symbol id="cog" viewBox="-12 -12 24 24">
        <path d="M-2-11h4l1 3 3-1.6 2.8 2.8L7.2-4 10-3v6l-3 1 1.6 3-2.8 2.8L3.8 8 2 11h-4l-1-3-3 1.6-2.8-2.8L-7.2 4-10 3v-6l3-1-1.6-3 2.8-2.8L-3.8-8z" fill="currentColor"/>
        <circle r="3.6" fill="#333"/>
      </symbol>
    </defs>
  </svg>

  <!-- stats bar -->
  <div class="statbar">
    <div class="view-switch"><div class="toggle" style="left:22px;top:8px"><span class="off">Just Me</span><span class="on">Everyone</span></div></div>
    <div class="stat" style="left:292px;border:0"><span class="ico"></span><span class="txt"><span class="num">3,458</span><br><span class="lbl">iMembers</span></span></div>
    <div class="stat" style="left:405px"><span class="ico"></span><span class="txt"><span class="num">1,700,250</span><br><span class="lbl">iPoints</span></span></div>
    <div class="stat" style="left:515px"><span class="ico"></span><span class="txt"><span class="num">800,125</span><br><span class="lbl">iActivity</span></span></div>
    <div class="stat" style="left:624px"><span class="ico"></span><span class="txt"><span class="num">600,100</span><br><span class="lbl">iNetworking</span></span></div>
    <div class="stat" style="left:747px"><span class="ico"></span><span class="txt"><span class="num">300,025</span><br><span class="lbl">iAttributes</span></span></div>
    <div class="stat" style="left:862px"><span class="ico"></span><span class="txt"><span class="num">i$900,125</span><br><span class="lbl">iDollars</span></span></div>
    <div class="stat" style="left:977px"><span class="ico"></span><span class="txt"><span class="num">900,000</span><br><span class="lbl">iShares</span></span></div>
  </div>

  <!-- header -->
  <div class="header">
    <div class="toggle" style="left:8px;top:8px"><span class="off">Detail</span><span class="on">Summary</span></div>
    <div class="brand">Gearwise</div>
    <div class="tagline">BUSINESS<br>SOLUTIONS<br>THROUGH<br>INSIGHT</div>
  </div>
  <div class="news" style="top:49px"><span class="ico"></span>The Advanced Search gives you 190,000+ permutations!</div>
  <div class="news" style="top:84px"><span class="ico"></span>Win i$100 for your feedback about our site</div>
  <div class="news" style="top:119px"><span class="ico"></span>Your Brand Ambassadors Are in the Building</div>
  <div class="news" style="top:154px"><span class="ico"></span>Dj</div>

  <!-- nav -->
  <nav class="nav">
    <div class="strip"></div>
    <div class="toggle" style="left:130px;top:6px"><span class="off">Insights</span><span class="on">Profile</span></div>
    <div class="tab home" style="left:270px">Home</div>
    <div class="tab" style="left:336px">Business Disciplines</div>
    <div class="tab" style="left:469px">Insights</div>
    <div class="tab active" style="left:536px">Solutions</div>
    <div class="tab" style="left:607px">Library</div>
    <div class="tab" style="left:664px">Rewards</div>
    <div class="tab" style="left:733px">Members</div>
    <div class="tab" style="left:808px">Specialists</div>
    <div class="tab" style="left:898px">Teams</div>
    <div class="tab home" style="left:957px;width:90px;gap:24px">
      <svg width="26" height="12" viewBox="0 0 26 12"><circle cx="6" cy="6" r="4.5" fill="none" stroke="#fff" stroke-width="2"/><path d="M10 6h15M20 6v4M24 6v3" stroke="#fff" stroke-width="2"/></svg>
      <svg width="20" height="18" viewBox="0 0 20 18"><circle cx="7" cy="5" r="4" fill="none" stroke="#fff" stroke-width="1.6"/><path d="M1 17c0-5 12-5 12 0M15 4v6M12 7h6" fill="none" stroke="#fff" stroke-width="1.6"/></svg>
    </div>
  </nav>

  <!-- login -->
  <div class="page"></div>
  <section class="card">
    <h1>Member Login</h1>
    <div class="rule"></div>
    <div class="field-label" style="left:58px;top:96px">Username or Email</div>
    <div class="field" style="left:58px;top:116px;width:178px"></div>
    <div class="field-label" style="left:58px;top:169px">Password</div>
    <div class="field" style="left:58px;top:189px;width:178px"></div>
    <div class="field-label" style="left:60px;top:243px">Please solve this sum to sign in</div>
    <div class="field" style="left:60px;top:263px;width:42px;height:32px"></div>
    <div class="field-label" style="left:110px;top:274px;font-size:12.5px;color:#ccc">- 1= Three</div>
    <div class="abs" style="left:55px;top:330px;width:270px;height:2px;background:linear-gradient(90deg,transparent,#bbb)"></div>
    <div class="login-btn">Log in</div>
    <div class="pill" style="left:502px;top:123px">Register</div>
    <div class="pill" style="left:522px;top:154px;width:155px">Forgot your Password</div>
    <div class="seal" style="left:268px;top:88px;width:270px;height:270px;background:radial-gradient(circle,#fff 0 40%,#e4e4e4 55%,#b5b5b5 80%,#6a6a6a 100%);box-shadow:0 0 18px rgba(0,0,0,.7)">
      <div class="seal" style="inset:18px;border:3px solid var(--orange)"></div>
      <div class="abs" style="left:0;right:0;top:112px;text-align:center;font-family:Montserrat,sans-serif;font-weight:800;font-size:36px;color:var(--ink)">Gearwise</div>
    </div>
    <svg class="abs" style="left:525px;top:295px" width="40" height="40" viewBox="0 0 40 40"><path d="M4 20 18 6v8c10 0 18 6 18 20-4-8-10-10-18-10v8z" fill="#888"/></svg>
    <div class="back" style="left:566px">Back to Gearwise<br>Insight</div>
  </section>

  <!-- footer -->
  <div class="stripes"></div>
  <footer class="footer"></footer>

  <svg class="abs" style="left:0;top:0" width="1201" height="1496" stroke="#8a8a8a" stroke-width="1" fill="none">
    <path d="M500 782V1090M425 1138v280M693 1138v280"/>
    <path d="M325 845l-30-25M340 848l15-25M305 848l-60-10M355 855l50-15M325 1015v25M300 1010l-40 20M352 1010l35 20"/>
    <path d="M277 1185l-5-25M255 1190l-40-20M300 1190l40-20M277 1355v25M250 1350l-35 25M305 1352l40 20"/>
    <path d="M559 1185v-20M535 1190l-50-20M585 1190l40-20M535 1350l-40 25M559 1355v20M585 1350l40 25"/>
    <path d="M832 1185v-20M808 1190l-45-15M858 1190l40-10M808 1350l-30 25M858 1350l40 20"/>
  </svg>

  <!-- key topics -->
  <div class="hub" style="left:240px;top:845px"><div class="mini">Gearwise</div><div class="title">KEY<br>TOPICS</div></div>
  <div class="lbl" style="left:258px;top:770px;text-align:center">Advanced<br>&nbsp;&nbsp;&nbsp;Search</div>
  <div class="lbl" style="left:333px;top:770px">Solution<br>Providers</div>
  <div class="lbl" style="left:207px;top:821px">Rewards</div>
  <div class="lbl hot" style="left:372px;top:821px">Affiliate Authors</div>
  <div class="lbl" style="left:230px;top:1045px">iDollars</div>
  <div class="lbl" style="left:309px;top:1058px;text-align:center">Power<br>Teams</div>
  <div class="lbl" style="left:370px;top:1044px;text-align:center">Improved<br>Employability</div>

  <!-- business disciplines -->
  <div class="hub" style="left:646px;top:840px"><div class="mini">Gearwise</div><div class="title">BUSINESS<br>DISCIPLINES</div></div>
  <svg class="abs" style="left:0;top:0;color:#bdbdbd" width="1201" height="1100">
    <use href="#cog" x="663" y="826" width="20" height="20"/><use href="#cog" x="692" y="812" width="20" height="20"/>
    <use href="#cog" x="723" y="808" width="20" height="20"/><use href="#cog" x="755" y="812" width="20" height="20"/>
    <use href="#cog" x="783" y="826" width="20" height="20" style="color:#f7941d"/><use href="#cog" x="807" y="847" width="20" height="20"/>
    <use href="#cog" x="825" y="874" width="20" height="20"/><use href="#cog" x="834" y="903" width="20" height="20"/>
    <use href="#cog" x="834" y="935" width="20" height="20"/><use href="#cog" x="825" y="965" width="20" height="20"/>
    <use href="#cog" x="808" y="993" width="20" height="20"/><use href="#cog" x="783" y="1014" width="20" height="20"/>
    <use href="#cog" x="755" y="1027" width="20" height="20"/><use href="#cog" x="723" y="1032" width="20" height="20"/>
    <use href="#cog" x="692" y="1027" width="20" height="20"/><use href="#cog" x="663" y="1014" width="20" height="20"/>
    <use href="#cog" x="639" y="993" width="20" height="20"/><use href="#cog" x="621" y="965" width="20" height="20"/>
    <use href="#cog" x="613" y="935" width="20" height="20"/><use href="#cog" x="613" y="903" width="20" height="20"/>
    <use href="#cog" x="621" y="874" width="20" height="20"/><use href="#cog" x="639" y="847" width="20" height="20"/>
  </svg>
  <div class="cat" style="left:670px;top:801px">ALL</div>
  <div class="cat" style="left:708px;top:777px">BUSINESS<br>ADVISORY</div>
  <div class="cat" style="left:772px;top:799px">BUSINESS ANALYTICS</div>
  <div class="cat r" style="right:545px;top:823px">SYSTEMS THINKING</div>
  <div class="cat r" style="right:570px;top:847px">STRATEGY</div>
  <div class="cat r" style="right:587px;top:876px">SOCIAL MEDIA</div>
  <div class="cat r" style="right:596px;top:907px">SALES</div>
  <div class="cat r" style="right:596px;top:936px">MONEY<br>MATTERS</div>
  <div class="cat r" style="right:590px;top:966px">PERFORMANCE<br>MANAGEMENT</div>
  <div class="cat r" style="right:572px;top:994px">NLP SUCCESS<br>COACHING</div>
  <div class="cat r" style="right:545px;top:1026px">MARKETING</div>
  <div class="cat r" style="right:513px;top:1044px">LEADERSHIP</div>
  <div class="cat hot" style="left:811px;top:823px">BUSINESS TOOLS</div>
  <div class="cat" style="left:835px;top:841px">CAREER<br>DEVELOPMENT</div>
  <div class="cat" style="left:853px;top:871px">CHANGE<br>MANAGEMENT</div>
  <div class="cat" style="left:862px;top:902px">CREATING<br>LEVERAGE</div>
  <div class="cat" style="left:864px;top:936px">CREATIVITY &amp;<br>INNOVATION</div>
  <div class="cat" style="left:852px;top:973px">CROWDSOURCING</div>
  <div class="cat" style="left:835px;top:1002px">ENTREPRENEURSHIP</div>
  <div class="cat" style="left:811px;top:1026px">FUTURE IDEAS</div>
  <div class="cat" style="left:778px;top:1044px">INTERNET SECURITY</div>
  <div class="cat" style="left:660px;top:1060px;width:140px;text-align:center">KNOWLEDGE,<br>TECHNOLOGY &amp; CULTURE</div>

  <!-- target audience -->
  <div class="hub" style="left:192px;top:1185px"><div class="mini">Gearwise</div><div class="title">TARGET<br>AUDIENCE</div></div>
  <div class="lbl" style="left:262px;top:1121px">MBAs</div>
  <div class="lbl" style="left:167px;top:1140px">Job seekers</div>
  <div class="lbl" style="left:324px;top:1140px">Authors</div>
  <div class="lbl" style="left:189px;top:1395px">Teams</div>
  <div class="lbl" style="left:247px;top:1414px">Individuals</div>
  <div class="lbl hot" style="left:316px;top:1395px">Entrepreneurs</div>

  <!-- library -->
  <div class="hub" style="left:474px;top:1185px"><div class="mini">Gearwise</div><div class="title" style="top:72px">LIBRARY</div></div>
  <div class="lbl" style="left:510px;top:1128px">Books</div>
  <div class="lbl" style="left:564px;top:1128px">Tutorials</div>
  <div class="lbl" style="left:448px;top:1163px">Articles</div>
  <div class="lbl hot" style="left:627px;top:1168px">Links</div>
  <div class="lbl" style="left:465px;top:1390px">Videos</div>
  <div class="lbl" style="left:539px;top:1405px">Insights</div>
  <div class="lbl" style="left:605px;top:1390px">Solutions</div>
  <svg class="abs" style="left:625px;top:1360px" width="26" height="26"><path d="M3 14l7 7L23 3" stroke="#ddd" stroke-width="2.5" fill="none"/></svg>

  <!-- community -->
  <div class="hub" style="left:747px;top:1185px"><div class="mini">Gearwise</div><div class="title" style="top:72px">COMMUNITY</div></div>
  <div class="lbl" style="left:772px;top:1128px">Affiliates</div>
  <div class="lbl" style="left:839px;top:1128px">Specialist</div>
  <div class="lbl" style="left:724px;top:1164px">Members</div>
  <div class="lbl" style="left:897px;top:1164px">Teams</div>
  <div class="lbl" style="left:738px;top:1390px">About Us</div>
  <div class="lbl hot" style="left:868px;top:1390px">Getting Started</div>
  <div class="lbl" style="left:778px;top:1416px">Terms &amp; Conditions</div>

  <!-- share and contact -->
  <div class="social" style="top:941px" aria-label="Share link"></div>
  <div class="social" style="top:979px" aria-label="Share link"></div>
  <div class="social" style="top:1017px" aria-label="Share link"></div>
  <div class="social" style="top:1054px" aria-label="Share link"></div>
  <div class="round" style="top:1117px"><svg width="18" height="10" viewBox="0 0 18 10"><path d="M1 7c4-6 12-6 16 0l-3 2-2-3c-2-1-4-1-6 0L4 9z" fill="#333"/></svg></div>
  <div class="round" style="top:1157px" aria-label="Call link"></div>
  <div class="round" style="top:1197px"><svg width="16" height="12" viewBox="0 0 16 12"><rect x="1" y="1" width="14" height="10" fill="#333"/><path d="M1 1l7 6 7-6" stroke="#9a9a9a" fill="none"/></svg></div>

  <div class="baseline"></div>
  <div class="foot-brand">Gearwise</div>
  <div class="copy">GEARWISE INSIGHT © 2014. ALL RIGHTS RESERVED.</div>
</div>
</body>
</html>
```